Stage Design Company Business Card

We are looking to step up up our business card design for our team.

We are a Full service Design and Consultation company for Stage and TV with an emphasis in Theatrical Lighting.

We like our materials to be clean and modern with solid colors free of patterns and gradients. Our brand consists of 4 primary colors Purple, Black, Grey, and White. Provided is our Word Mark as well as our Symbol Logo.

We would like our cards to leave an impression beyond the information, show our attention to design and detail, and make our marks an easily recognized feature (together or apart) for our clients.

We need a warm approachable comfortable feel for some clients, and a professional flair for the board member type clients.

Attached are our brand elements, and our existing cards to give a sense of our style and a glipse at the information we provide on our cards.

Target Market(s)

broad client base from church leaders to high school teachers and architects.

Industry/Entity Type

Business

Contact Information for Business Card

We format our phone number with periods not parenthesis or dashes. Information will be edited for each of our team members, and team member specific cards are not part of this scope, but rather a template so to speak.

Font styles to use
Sans Serif

Colors
6b449b
ffffff
000000
333333
aaaaaa

Requirements
Must have
• Wordmark and logo mark present (does not need to exist on the same side of card)
• Brand Colors,
• Name, Phone, Email, Address.
• Unique choices that make someone stop and take a second look
Nice to have
• It would be nice to somehow convey what we DO, as our brand name does not lend itself to this, outside of an obvious tagline though.....
• social media if not crowded. all of our handles match (instagram, twitter, facebook)
Should not have
• "clipart"

```html
<!DOCTYPE html>
<html lang="en">
<head>
<meta charset="utf-8">
<title>Halvor Stage — Business Card</title>
<link rel="stylesheet" href="https://fonts.googleapis.com/css2?family=Jost:wght@400;500;700&display=swap">
<style>
  :root {
    --backdrop: #8e8d8e;
    --brand-purple: #3a2368;
    --paper: #ffffff;
    --ink: #333333;
    --shadow: rgba(0, 0, 0, 0.28);
  }
  * { box-sizing: border-box; margin: 0; padding: 0; }
  html, body {
    width: 1200px;
    height: 929px;
    overflow: hidden;
    background: var(--backdrop);
    font-family: "Jost", sans-serif;
  }
  .canvas {
    position: relative;
    width: 1200px;
    height: 929px;
  }
  .card {
    position: absolute;
    left: 300px;
    width: 600px;
    height: 343px;
    box-shadow: 0 6px 14px var(--shadow);
  }
  .card-front {
    top: 96px;
    background: var(--brand-purple);
    display: flex;
    flex-direction: column;
    align-items: center;
    justify-content: center;
    gap: 14px;
  }
  .card-back {
    top: 490px;
    background: var(--paper);
  }
  .brand-lockup {
    display: flex;
    align-items: center;
    gap: 12px;
  }
  .brand-dot {
    width: 14px;
    height: 14px;
    border-radius: 50%;
  }
  .brand-name {
    font-weight: 500;
    letter-spacing: 0.32em;
    text-transform: uppercase;
  }
  .card-front .brand-dot { background: var(--paper); }
  .card-front .brand-name { color: var(--paper); font-size: 26px; }

  .back-frame {
    position: absolute;
    inset: 22px;
    border: 2px solid var(--brand-purple);
  }
  .card-back .brand-lockup {
    position: absolute;
    right: 56px;
    top: 78px;
  }
  .card-back .brand-dot { background: var(--brand-purple); width: 11px; height: 11px; }
  .card-back .brand-name { color: var(--brand-purple); font-size: 18px; }

  .person {
    position: absolute;
    left: 64px;
    top: 112px;
  }
  .person-name {
    font-weight: 700;
    font-size: 22px;
    color: var(--brand-purple);
    text-transform: uppercase;
    letter-spacing: 0.01em;
  }
  .person-role {
    font-size: 13px;
    color: var(--ink);
    text-transform: uppercase;
    margin-top: 2px;
  }
  .contact {
    position: absolute;
    left: 64px;
    top: 200px;
    color: var(--ink);
    font-size: 14px;
    line-height: 1.2;
  }
  .contact-address { margin-bottom: 8px; }
  .contact-list { list-style: none; }
  .contact-list li {
    display: flex;
    align-items: center;
    gap: 8px;
    margin-bottom: 3px;
    font-size: 15px;
  }
  .contact-icon {
    width: 15px;
    height: 15px;
    flex: none;
  }
</style>
</head>
<body>
<main class="canvas">
  <section class="card card-front" aria-label="Card front">
    <div class="brand-lockup">
      <span class="brand-dot"></span>
      <span class="brand-name">Halvor Stage</span>
    </div>
  </section>

  <section class="card card-back" aria-label="Card back">
    <div class="back-frame"></div>

    <div class="person">
      <p class="person-name">Mara L Quinn</p>
      <p class="person-role">Owner</p>
    </div>

    <div class="contact">
      <p class="contact-address">52 N. Orchard Ave Tempe,<br>AZ 85281</p>
      <ul class="contact-list">
        <li>
          <svg class="contact-icon" viewBox="0 0 16 16" aria-hidden="true">
            <rect width="16" height="16" rx="2" fill="#3a2368"/>
            <path d="M4.5 3.5l2 .3.6 2-1.2 1a6 6 0 0 0 3.3 3.3l1-1.2 2 .6.3 2c-.3.6-1 1-1.6 1C6.4 12.4 3.6 9.6 3.5 5.1c0-.6.4-1.3 1-1.6z" fill="#fff"/>
          </svg>
          <span>800.555.0143</span>
        </li>
        <li>
          <svg class="contact-icon" viewBox="0 0 16 16" aria-hidden="true">
            <rect width="16" height="16" rx="2" fill="#3a2368"/>
            <rect x="3" y="4.5" width="10" height="7" fill="none" stroke="#fff" stroke-width="1.3"/>
            <path d="M3 4.5l5 4 5-4" fill="none" stroke="#fff" stroke-width="1.3"/>
          </svg>
          <span>hello@halvor-stage.com</span>
        </li>
        <li>
          <svg class="contact-icon" viewBox="0 0 16 16" aria-hidden="true">
            <rect width="16" height="16" rx="2" fill="#3a2368"/>
            <circle cx="7" cy="7" r="3.2" fill="none" stroke="#fff" stroke-width="1.4"/>
            <path d="M9.4 9.4l3 3" stroke="#fff" stroke-width="1.6" stroke-linecap="round"/>
          </svg>
          <span>halvor-stage.com</span>
        </li>
      </ul>
    </div>

    <div class="brand-lockup">
      <span class="brand-dot"></span>
      <span class="brand-name">Halvor Stage</span>
    </div>
  </section>
</main>
</body>
</html>
```